Web Site Redesign

We operate a data centre facility specialing in colocation and Fibre optic connectivity (i.e. point to point fibre services and internet over fibre).

We have an existing site located at www.corvanlink.example however this is very very tired and requires a redesign. We are looking for a fresh new design that will be appealing to potential customers.

The Company name is Corvan Lk and the primary corporate colour is bright red with secondary colours of white, grey and black. Specific bright red can be seen in attached company logo.

Website needs to be modern, clean and professional representing our premium colocation and fibre provider branding.

Our company slogan is : safe. secure. reliable

We will provide feedback regardless of the quality of the design to ensure a better outcome for all parties.

Please feel free to contact us if you have any questions.

# The designer can use placeholder images or feel free to use any/all or none of the attached images
# The designer can use sample filler text

Target Market(s)

Technical IT Professionals as well C level executives (i.e. CEO's, CIO).

Industry/Entity Type

Internet

Requirements
Must have
• clean design
Nice to have
• A sidebar with two sections. 1 for current promo and 1 for "Let us call you back/contact you"
Should not have
• Clutter

```html
<!DOCTYPE html>
<html lang="en">
<head>
<meta charset="utf-8">
<title>About Us – Corvan Lk Data Centre</title>
<link href="https://fonts.googleapis.com/css2?family=Arimo:ital,wght@0,400;0,700;1,400&display=swap" rel="stylesheet">
<style>
:root{
  --page:#f2eeed;
  --red:#c9272c;
  --red-dark:#b01f24;
  --black:#000;
  --ink:#111;
  --white:#fff;
  --line:#dcd6d4;
  --grey:#9a9a9a;
}
*{margin:0;padding:0;box-sizing:border-box}
html,body{width:1200px;height:849px;overflow:hidden}
body{background:var(--page);font-family:Arimo,Arial,sans-serif;color:var(--ink);position:relative}
.abs{position:absolute}
a{color:inherit;text-decoration:none}

.brand{left:110px;top:100px;display:flex;align-items:center;gap:7px}
.brand-mark{width:18px;height:18px;background:var(--red)}
.brand-name{font-size:23px;line-height:26px;color:var(--red);font-weight:700;white-space:nowrap}

.tagline{left:263px;top:22px}
.tagline .city{font-size:14px}
.tagline .slogan{font-size:30px;font-style:italic;line-height:32px;letter-spacing:-.3px}
.tagline .sub{font-size:13px;text-align:right;margin-top:-2px}

.contact{right:118px;top:33px;text-align:right;font-size:12.5px;line-height:20px}
.contact span{display:inline-flex;align-items:center;gap:6px}
.contact svg{display:block}

.nav{left:261px;top:100px;width:823px;height:37px;background:var(--red);display:flex}
.nav a{color:var(--white);font-size:14px;display:flex;align-items:center;justify-content:center;height:37px}
.nav a.active{background:var(--black)}

.banner{left:103px;top:141px;width:982px;height:100px;background:var(--red);overflow:hidden}
.banner h1{position:absolute;left:25px;top:33px;color:var(--white);font-size:29px;font-weight:400;font-style:italic}
.banner-photo{position:absolute;right:0;top:0;width:460px;height:100px;background:linear-gradient(90deg,var(--red) 0%,#8a3a30 30%,#3a3533 60%,#d48a50 85%,#c9b89a 100%)}

.panel{background:var(--white);border:1px solid var(--line)}
.crumbs{left:103px;top:249px;width:981px;height:27px;font-size:11px;display:flex;align-items:center;justify-content:space-between;padding:0 12px}
.crumbs .here{color:var(--red)}

.main{left:103px;top:287px;width:759px;height:346px}
.main-photo{position:absolute;left:20px;top:18px;width:222px;height:132px;background:linear-gradient(135deg,#b9a07a,#d33a2e 45%,#2c2a2a 75%,#5a5a55)}
.main h2{position:absolute;left:261px;top:22px;font-size:17px;color:var(--red);font-weight:400}
.copy{position:absolute;left:20px;top:59px;width:720px;font-size:11.2px;line-height:18px}
.copy p{margin-bottom:18px}
.copy .indent{padding-left:241px}
.copy .after{margin-top:12px}
.copy em{font-style:normal;color:var(--red)}
.cta{position:absolute;left:20px;top:284px;font-size:13.5px;font-weight:700;white-space:nowrap}
.cta a{color:var(--red)}

.side{left:868px;top:287px;width:216px;height:346px}
.side-photo{position:absolute;left:4px;top:3px;width:206px;height:107px;background:linear-gradient(135deg,#d8d4cc,#9a9894 50%,#3c3c3e)}
.side h3{position:absolute;left:11px;top:121px;font-size:14px;font-weight:400;padding-bottom:6px;border-bottom:1px dotted #555;width:185px}
.side h3 b{color:var(--red);font-weight:400}
.services{position:absolute;left:11px;top:154px;list-style:none;font-size:11.5px;line-height:20px}
.services li{display:flex;align-items:center;gap:9px}
.services li::before{content:"";width:8px;height:8px;border-radius:50%;background:var(--red)}
.more{position:absolute;left:134px;top:315px;width:68px;height:20px;background:var(--red);color:var(--white);font-size:11px;display:flex;align-items:center;justify-content:center}

.partners{left:103px;top:640px;width:981px;height:117px;overflow:hidden}
.ribbon{position:absolute;left:-1px;top:-1px}
.partner{position:absolute;background:#e6e3e2;border-radius:4px}

.rule{left:102px;top:767px;width:982px;height:4px;background:var(--black)}
.legal{left:105px;top:784px;font-size:11px;line-height:18px}
.legal .links{color:var(--red)}
.legal .links i{font-style:normal;color:var(--ink);margin:0 7px}
.social{right:116px;top:783px;display:flex;gap:5px}
.social a{width:68px;height:20px;font-size:11px;color:var(--white);display:flex;align-items:center;justify-content:center}
.social .dark{background:var(--black)}
.social .red{background:var(--red)}
</style>
</head>
<body>

<div class="abs brand"><span class="brand-mark"></span><span class="brand-name">Corvan Lk</span></div>

<div class="abs tagline">
  <div class="city">Perth’s</div>
  <div class="slogan">Save, Secure &amp; Reliable</div>
  <div class="sub">Data Centre</div>
</div>

<div class="abs contact">
  <span>sales@corvanlink.example
    <svg width="15" height="10" viewBox="0 0 15 10"><rect width="15" height="10" fill="#c9272c"/><path d="M0 0l7.5 6L15 0" stroke="#fff" fill="none"/></svg></span><br>
  <span>+1 555 010 472
    <svg width="15" height="11" viewBox="0 0 15 11"><path d="M1 4c0-3 13-3 13 0v2h-3V4H4v2H1z" fill="#c9272c"/><rect x="3" y="6" width="9" height="5" fill="#c9272c"/></svg></span>
</div>

<nav class="abs nav">
  <a href="#" style="width:82px">Home</a>
  <a href="#" class="active" style="width:86px">About Us</a>
  <a href="#" style="width:106px">Facilities ▾</a>
  <a href="#" style="width:88px">Business</a>
  <a href="#" style="width:100px">Continuity</a>
  <a href="#" style="width:86px">Services</a>
  <a href="#" style="width:98px">Partners</a>
  <a href="#" style="width:88px">Webmail</a>
  <a href="#" style="width:89px">Contact Us</a>
</nav>

<header class="abs banner">
  <div class="banner-photo" role="img" aria-label="Close-up of orange fibre patch cables plugged into a switch"></div>
  <h1>It’s All About Us</h1>
</header>

<div class="abs panel crumbs">
  <div><span class="here">You’re Here :</span>&nbsp; Home :: About Us</div>
  <div>Monday, August 16 2010</div>
</div>

<main class="abs panel main">
  <div class="main-photo" role="img" aria-label="Data centre floor with red wall and server racks"></div>
  <h2>About Corvan Lk</h2>
  <div class="copy">
    <p class="indent">Corvan Lk is a world-class datacentre in one of the safest places on earth. We are located in the most remote city in the world.</p>
    <p class="indent" style="margin-bottom:0">Built around the resources sector, the city services the oil and mining industries in the state and surrounding regions. The Asian economic crisis (which affected mining prices)</p>
    <p class="after">and the dot-com boom in the late 90’s and early 00’s motivated quite a few resources companies to invest heavily on IT infrastructure. This resulted in one of the most wired and techno-savvy cities in the country. <em>CorvanLk</em> was a product of this heavy investment phase. An amazing $3.6 million was spent on the <em>facility</em> which boasted the very best of everything. The latest from Norvex, Brightwave and Tarrow - not to mention the triple redundant power systems including an oversized generator, biometric readers, proximity cards and motion sensitive image recording system. To truly appreciate the facility that boasts a 100% uptime on the SLAs (Power, Environment, Temperature and Access) since commencement,</p>
  </div>
  <div class="cta">please call us on (08) 5550 1472 to have a tour organised or you can found us <a href="#">here</a>.</div>
</main>

<aside class="abs panel side">
  <div class="side-photo" role="img" aria-label="Woman working on a laptop"></div>
  <h3>OUR <b>SERVICES</b></h3>
  <ul class="services">
    <li>Co-location</li>
    <li>Fibre connectivity</li>
    <li>Web Hosting</li>
    <li>Remote offsite backups</li>
    <li>Managed and hosted software</li>
    <li>solutions</li>
    <li>Internet Connectivity via Fibre</li>
  </ul>
  <a href="#" class="more">Read More</a>
</aside>

<section class="abs panel partners" aria-label="Our partners">
  <svg class="ribbon" width="100" height="90" viewBox="0 0 100 90">
    <path d="M75 0H97L0 85V63z" fill="#c9272c"/>
    <text x="0" y="0" fill="#fff" font-family="Arimo,Arial,sans-serif" font-size="9" transform="translate(8 68) rotate(-41)">OUR PARTNERS</text>
  </svg>
  <div class="partner" style="left:73px;top:22px;width:122px;height:76px"></div>
  <div class="partner" style="left:230px;top:26px;width:195px;height:68px"></div>
  <div class="partner" style="left:460px;top:34px;width:188px;height:44px"></div>
  <div class="partner" style="left:671px;top:32px;width:140px;height:58px"></div>
</section>

<div class="abs rule"></div>
<footer class="abs legal">
  <div>Copyright © 2010 by CorvanLk. All Right Reserved.</div>
  <div class="links"><a href="#">Term Of Use</a><i>|</i><a href="#">Privacy Policy</a><i>|</i><a href="#">Contact Us</a></div>
</footer>
<div class="abs social">
  <a href="#" class="dark">Friendly</a>
  <a href="#" class="dark">Chirper</a>
  <a href="#" class="red">XHTML</a>
  <a href="#" class="red">CSS</a>
</div>

</body>
</html>
```